Business Card Design

WE are looking for a premium quality Business Cards for a Law Firm . Copies of our current business card is attached.
Updates

Went on vacation/holiday

Contact Information for Business Card

xyz

```html
<!DOCTYPE html>
<html lang="en">
<head>
<meta charset="utf-8">
<title>Harrowgate Lawyers – Business Cards</title>
<link href="https://fonts.googleapis.com/css2?family=Montserrat:wght@400;500;600;700&display=swap" rel="stylesheet">
<style>
  :root{
    --bg:#3a3a3a;
    --green:#0f2a1d;
    --green-deep:#08210f;
    --gold:#c9a461;
    --white:#ffffff;
    --rule:rgba(255,255,255,.35);
  }
  *{margin:0;padding:0;box-sizing:border-box}
  html,body{width:1200px;height:1200px;overflow:hidden}
  body{background:var(--bg);font-family:'Montserrat',sans-serif;position:relative}
  .card{position:absolute;left:150px;width:900px;height:514px;border-radius:28px;overflow:hidden;box-shadow:0 14px 30px rgba(0,0,0,.45)}
  .card--front{top:50px;background:linear-gradient(120deg,var(--green-deep) 0%,var(--green) 55%,#16392a 75%,var(--green-deep) 100%)}
  .card--back{top:630px;background:var(--white)}

  /* front */
  .person{position:absolute;left:60px;top:120px;width:330px}
  .person__name{color:var(--gold);font-weight:700;font-size:40px;letter-spacing:.5px;line-height:1}
  .person__title{color:var(--white);font-size:13px;font-weight:500;line-height:1.25;margin-top:8px;text-transform:uppercase}
  .contacts{list-style:none;margin-top:22px}
  .contacts li{display:flex;align-items:center;gap:12px;color:var(--white);font-size:15px;margin-bottom:11px}
  .icon{width:28px;height:28px;border-radius:50%;background:var(--gold);display:flex;align-items:center;justify-content:center;flex:none}
  .icon svg{width:15px;height:15px}
  .divider{position:absolute;width:1px;background:var(--rule)}
  .card--front .divider{left:420px;top:110px;height:200px}
  .brand{position:absolute;display:flex;flex-direction:column;align-items:center}
  .brand__mark{width:78px;height:78px;border-radius:50%;border:4px solid var(--gold)}
  .brand__name{font-weight:600;font-size:34px;letter-spacing:3px;margin-top:18px;line-height:1.15;text-align:center}
  .card--front .brand{left:470px;top:120px;width:400px}
  .card--front .brand__name{color:var(--white)}
  .address{position:absolute;left:0;right:0;top:390px;text-align:center;color:var(--white);font-size:21px;line-height:1.4;padding-left:200px}

  /* back */
  .card--back .brand{left:0;right:0;top:45px}
  .card--back .brand__name{color:var(--green)}
  .band-gold{position:absolute;left:0;right:0;top:298px;height:7px;background:var(--gold)}
  .band-green{position:absolute;left:0;right:0;top:314px;bottom:0;background:linear-gradient(120deg,var(--green-deep) 0%,var(--green) 50%,#16392a 70%,var(--green-deep) 100%)}
  .office{position:absolute;top:345px;width:360px;color:var(--white);font-size:14px;line-height:1.45}
  .office--brisbane{left:80px}
  .office--melbourne{left:500px}
  .office__label{color:var(--gold);font-weight:600;font-size:15px;text-transform:uppercase;margin-bottom:6px}
  .office__row{display:flex;gap:10px;align-items:flex-start;margin-bottom:6px}
  .office__row svg{width:16px;height:16px;flex:none;margin-top:2px}
  .card--back .divider{left:465px;top:350px;height:110px}
</style>
</head>
<body>

<section class="card card--front">
  <div class="person">
    <h1 class="person__name">DANIEL REYES</h1>
    <p class="person__title">Director &amp; Principal Solicitor<br>MBA, Juris Doctor</p>
    <ul class="contacts">
      <li><span class="icon"><svg viewBox="0 0 24 24"><path fill="#0f2a1d" d="M6.6 10.8a15 15 0 0 0 6.6 6.6l2.2-2.2a1 1 0 0 1 1-.25 11.4 11.4 0 0 0 3.6.57 1 1 0 0 1 1 1V20a1 1 0 0 1-1 1A17 17 0 0 1 3 4a1 1 0 0 1 1-1h3.5a1 1 0 0 1 1 1c0 1.25.2 2.45.57 3.57a1 1 0 0 1-.25 1z"/></svg></span>+61 7 3000 4182</li>
      <li><span class="icon"><svg viewBox="0 0 24 24"><rect x="6" y="2" width="12" height="20" rx="2" fill="none" stroke="#0f2a1d" stroke-width="2"/><circle cx="12" cy="18" r="1.3" fill="#0f2a1d"/></svg></span>+61 0400 271 936</li>
      <li><span class="icon"><svg viewBox="0 0 24 24"><rect x="3" y="5" width="18" height="14" rx="1.5" fill="none" stroke="#0f2a1d" stroke-width="2"/><path d="M3 6l9 7 9-7" fill="none" stroke="#0f2a1d" stroke-width="2"/></svg></span>daniel@harrowgatelawyers.com.au</li>
      <li><span class="icon"><svg viewBox="0 0 24 24" fill="none" stroke="#0f2a1d" stroke-width="1.8"><circle cx="12" cy="12" r="9"/><ellipse cx="12" cy="12" rx="4" ry="9"/><path d="M3 12h18M5 7h14M5 17h14"/></svg></span>www.harrowgatelawyers.com.au</li>
    </ul>
  </div>
  <div class="divider"></div>
  <div class="brand">
    <span class="brand__mark"></span>
    <span class="brand__name">HARROWGATE<br>LAWYERS</span>
  </div>
  <p class="address">Level 3, Harrow House,<br>82 Ardent Terrace, Spring Hill, QLD 4000</p>
</section>

<section class="card card--back">
  <div class="brand">
    <span class="brand__mark"></span>
    <span class="brand__name">HARROWGATE<br>LAWYERS</span>
  </div>
  <div class="band-gold"></div>
  <div class="band-green"></div>
  <div class="office office--brisbane">
    <p class="office__label">Brisbane Office</p>
    <div class="office__row"><svg viewBox="0 0 24 24"><path fill="none" stroke="#c9a461" stroke-width="2.4" d="M12 22s7-7 7-12a7 7 0 0 0-14 0c0 5 7 12 7 12z"/><circle cx="12" cy="10" r="2.5" fill="#c9a461"/></svg><span>Level 3, Harrow House, 82<br>Ardent Terrace Spring Hill QLD 4000</span></div>
    <div class="office__row"><svg viewBox="0 0 24 24"><path fill="#c9a461" d="M6.6 10.8a15 15 0 0 0 6.6 6.6l2.2-2.2a1 1 0 0 1 1-.25 11.4 11.4 0 0 0 3.6.57 1 1 0 0 1 1 1V20a1 1 0 0 1-1 1A17 17 0 0 1 3 4a1 1 0 0 1 1-1h3.5a1 1 0 0 1 1 1c0 1.25.2 2.45.57 3.57a1 1 0 0 1-.25 1z"/></svg><span>(07) 3000 4182</span></div>
  </div>
  <div class="divider"></div>
  <div class="office office--melbourne">
    <p class="office__label">Melbourne Office</p>
    <div class="office__row"><svg viewBox="0 0 24 24"><path fill="none" stroke="#c9a461" stroke-width="2.4" d="M12 22s7-7 7-12a7 7 0 0 0-14 0c0 5 7 12 7 12z"/><circle cx="12" cy="10" r="2.5" fill="#c9a461"/></svg><span>Suite 205, Kestrel Chambers, 218<br>Linden Street, Melbourne, VIC, 3000</span></div>
    <div class="office__row"><svg viewBox="0 0 24 24"><path fill="#c9a461" d="M6.6 10.8a15 15 0 0 0 6.6 6.6l2.2-2.2a1 1 0 0 1 1-.25 11.4 11.4 0 0 0 3.6.57 1 1 0 0 1 1 1V20a1 1 0 0 1-1 1A17 17 0 0 1 3 4a1 1 0 0 1 1-1h3.5a1 1 0 0 1 1 1c0 1.25.2 2.45.57 3.57a1 1 0 0 1-.25 1z"/></svg><span>(07) 3000 4182</span></div>
  </div>
</section>

</body>
</html>
```